Romantic Experiences Business Needs Banner Ad Design Project

We are going to run a branding campaign and we need banner ad design for a company based in Mexico City called "CIRANDELLA".

We create romantic experiences or moments for couples celebrating special dates, for instance birthdays, wedding anniversaries and original ways to give an engagement ring. These experiences may have components like romantic dinner, chamber musicians, astronomer, concierges, fireworks, mansions, romantic tours on helicopter and yacht.

The final design should communicate our main task "romantic moment design" and brand attributes: sophisticated, elegant and romantic.

You can visit the webpage at: http://www.cirandella-example.com.mx

Target Market(s)

People from 25 to 50 years old who wants to celebrate wedding anniversary or give an engagement ring

Industry/Entity Type

Wedding

Requirements
Must have
• - Logo
- Banner sizes: 300x250, 728x90,160x600
Nice to have
• - Call to Action
- Theme: "Diseño Momentos Románticos"

```html
<!DOCTYPE html>
<html lang="es">
<head>
<meta charset="utf-8">
<title>CIRANDELLA – Banners</title>
<link href="https://fonts.googleapis.com/css2?family=Oswald:wght@300;400&display=swap" rel="stylesheet">
<style>
:root{
  --bg:#1c1c1c;
  --bg-2:#2a2a2a;
  --pink:#c8175a;
  --pink-light:#e2457f;
  --pink-dark:#9e0c3e;
  --white:#ffffff;
  --logo-grey:#6a6a6a;
  --silver-1:#fbfbfb;
  --silver-2:#cfcfcf;
  --btn-text:#c8175a;
  --stripe:#7a7a7a;
}
*{margin:0;padding:0;box-sizing:border-box}
html,body{width:1200px;height:664px;overflow:hidden}
body{background:linear-gradient(135deg,var(--bg-2),var(--bg) 60%,#151515);font-family:"Oswald",sans-serif;position:relative}
.banner{position:absolute;overflow:hidden;background:var(--white)}
.photo{position:absolute}
.photo.color{background:linear-gradient(120deg,#e8d2b8 0%,#d9b08c 35%,#6b4a3a 60%,#c9c9cf 85%,#9db58a 100%)}
.photo.mono{background:linear-gradient(120deg,#e2e2e2 0%,#bdbdbd 35%,#4a4a4a 60%,#cfcfcf 85%,#9a9a9a 100%)}
.band{position:absolute;background:radial-gradient(ellipse at 70% 40%,var(--pink-light),var(--pink) 55%,var(--pink-dark))}
.logo{position:absolute;text-align:center;color:var(--logo-grey);font-weight:300;letter-spacing:.04em;line-height:1}
.tagline{display:block;font-size:.22em;letter-spacing:.35em;color:var(--pink);margin-top:.35em}
.headline{position:absolute;color:var(--white);text-align:center;font-weight:400;line-height:1.05;text-shadow:0 2px 3px rgba(0,0,0,.35)}
.cta{position:absolute;border-radius:5px;background:linear-gradient(var(--silver-1),var(--silver-2));border:1px solid #9a9a9a;box-shadow:0 2px 4px rgba(0,0,0,.4);color:var(--btn-text);display:flex;align-items:center;justify-content:center;font-weight:400}
/* skyscraper 160x600 */
.sky{top:21px;width:165px;height:617px}
.sky .logo{top:6px;left:0;width:100%;font-size:21px}
.sky .photo{top:36px;left:0;width:100%;height:345px}
.sky .band{top:376px;left:0;width:100%;height:241px;border-top:6px solid var(--stripe)}
.sky .headline{top:412px;left:0;width:100%}
.sky .h1{font-size:52px;display:block}
.sky .h2{font-size:33px;display:block}
.sky .h3{font-size:29px;display:block}
.sky .cta{left:12px;top:574px;width:141px;height:36px;font-size:19px}
/* rectangle 300x250 */
.rect{top:41px;width:347px;height:288px}
.rect .logo{top:10px;left:0;width:100%;font-size:40px}
.rect .photo{top:66px;left:0;width:100%;height:170px}
.rect svg{position:absolute;left:0;top:195px}
.rect .cta{left:112px;top:214px;width:142px;height:32px;font-size:18px}
.rect .headline{top:252px;left:0;width:100%;font-size:25px}
/* leaderboard 728x90 */
.board{left:417px;width:750px;height:92px;background:transparent}
.board .photo{left:0;top:0;width:240px;height:100%}
.board svg{position:absolute;left:0;top:0}
.board .headline{left:255px;top:4px;width:230px}
.board .l1{display:block;font-size:27px}
.board .l2{display:block;font-size:39px}
.board .logo{left:530px;top:6px;width:200px;font-size:25px;color:var(--white)}
.board .logo .tagline{color:var(--white);font-size:.28em}
.board .cta{left:550px;top:44px;width:165px;height:40px;font-size:21px}
</style>
</head>
<body>

<!-- Skyscrapers -->
<section class="banner sky" style="left:28px">
  <div class="logo">CIRANDELLA<span class="tagline">EXPERIENCIAS ROMÁNTICAS</span></div>
  <div class="photo color" role="img" aria-label="Fotografía de una pareja abrazándose"></div>
  <div class="band"></div>
  <h2 class="headline"><span class="h1">DISEÑO</span><span class="h2">MOMENTOS</span><span class="h3">ROMÁNTICOS</span></h2>
  <div class="cta">APRENDE MÁS!</div>
</section>

<section class="banner sky" style="left:218px">
  <div class="logo">CIRANDELLA<span class="tagline">EXPERIENCIAS ROMÁNTICAS</span></div>
  <div class="photo mono" role="img" aria-label="Fotografía en blanco y negro de una pareja abrazándose"></div>
  <div class="band"></div>
  <h2 class="headline"><span class="h1">DISEÑO</span><span class="h2">MOMENTOS</span><span class="h3">ROMÁNTICOS</span></h2>
  <div class="cta">APRENDE MÁS!</div>
</section>

<!-- Medium rectangles -->
<section class="banner rect" style="left:417px">
  <div class="logo">CIRANDELLA<span class="tagline">EXPERIENCIAS ROMÁNTICAS</span></div>
  <div class="photo mono" role="img" aria-label="Fotografía en blanco y negro de una pareja sonriendo"></div>
  <svg width="347" height="93" viewBox="0 0 347 93">
    <defs><radialGradient id="rp1" cx="70%" cy="50%" r="80%"><stop offset="0" stop-color="#e2457f"/><stop offset=".55" stop-color="#c8175a"/><stop offset="1" stop-color="#9e0c3e"/></radialGradient></defs>
    <path d="M0 14 Q173 48 347 0 L347 93 L0 93Z" fill="#7a7a7a"/>
    <path d="M0 20 Q173 54 347 6 L347 93 L0 93Z" fill="url(#rp1)"/>
  </svg>
  <div class="cta">APRENDE MÁS!</div>
  <h2 class="headline">DISEÑO MOMENTOS ROMÁNTICOS</h2>
</section>

<section class="banner rect" style="left:792px">
  <div class="logo">CIRANDELLA<span class="tagline">EXPERIENCIAS ROMÁNTICAS</span></div>
  <div class="photo color" role="img" aria-label="Fotografía de una pareja sonriendo en un jardín"></div>
  <svg width="347" height="93" viewBox="0 0 347 93">
    <defs><radialGradient id="rp2" cx="70%" cy="50%" r="80%"><stop offset="0" stop-color="#e2457f"/><stop offset=".55" stop-color="#c8175a"/><stop offset="1" stop-color="#9e0c3e"/></radialGradient></defs>
    <path d="M0 14 Q173 48 347 0 L347 93 L0 93Z" fill="#7a7a7a"/>
    <path d="M0 20 Q173 54 347 6 L347 93 L0 93Z" fill="url(#rp2)"/>
  </svg>
  <div class="cta">APRENDE MÁS!</div>
  <h2 class="headline">DISEÑO MOMENTOS ROMÁNTICOS</h2>
</section>

<!-- Leaderboards -->
<section class="banner board" style="top:416px">
  <div class="photo color" role="img" aria-label="Fotografía de una pareja abrazándose"></div>
  <svg width="750" height="92" viewBox="0 0 750 92">
    <defs><radialGradient id="lp1" cx="60%" cy="50%" r="70%"><stop offset="0" stop-color="#e2457f"/><stop offset=".55" stop-color="#c8175a"/><stop offset="1" stop-color="#9e0c3e"/></radialGradient></defs>
    <path d="M208 0 Q240 46 230 92 L750 92 L750 0Z" fill="#7a7a7a"/>
    <path d="M216 0 Q248 46 238 92 L750 92 L750 0Z" fill="url(#lp1)"/>
  </svg>
  <h2 class="headline"><span class="l1">DISEÑO MOMENTOS</span><span class="l2">ROMÁNTICOS</span></h2>
  <div class="logo">CIRANDELLA<span class="tagline">EXPERIENCIAS ROMÁNTICAS</span></div>
  <div class="cta">APRENDE MÁS!</div>
</section>

<section class="banner board" style="top:527px">
  <div class="photo mono" role="img" aria-label="Fotografía en blanco y negro de una pareja abrazándose"></div>
  <svg width="750" height="92" viewBox="0 0 750 92">
    <defs><radialGradient id="lp2" cx="60%" cy="50%" r="70%"><stop offset="0" stop-color="#e2457f"/><stop offset=".55" stop-color="#c8175a"/><stop offset="1" stop-color="#9e0c3e"/></radialGradient></defs>
    <path d="M208 0 Q240 46 230 92 L750 92 L750 0Z" fill="#7a7a7a"/>
    <path d="M216 0 Q248 46 238 92 L750 92 L750 0Z" fill="url(#lp2)"/>
  </svg>
  <h2 class="headline"><span class="l1">DISEÑO MOMENTOS</span><span class="l2">ROMÁNTICOS</span></h2>
  <div class="logo">CIRANDELLA<span class="tagline">EXPERIENCIAS ROMÁNTICAS</span></div>
  <div class="cta">APRENDE MÁS!</div>
</section>

</body>
</html>
```